Create a Capability Summary in PowerPoint

CAPABILITY SUMMARY:
We have been asked to provide a Capability Summary by a client and we need your help creating a compelling document!
Our firm specializes in placing cleared technical talent with innovative government contracting firms nationwide. Our goal is to position ourselves as the "go to" talent acquisition company for small and large IT contracting firms in the Federal IT market.
We want you to have creative control over this template, but would like to it include some variation of the following:
Cover Slide w/ Logo
About Us
The Vantrel Difference
Benefits We Offer
-noting that, unlike many recruiting forms, we offer generous PTO, 100%
vesting 401K, and healthcare benefits for all employees
The Talent We Work With
-showcase the fact that we work in the following technical areas:
Network & Systems Engineer, Software Development, Data Science,
and Information Assurance
Clients We Work With
Data-Driven Recruiting Process
-funnel or graphic showcasing our multi-stage recruiting process of :
Sourcing -> Data Discovery -> Automated Outreach -> Candidate
Qualification -> Technical Interview -> Offer & On-boarding
Contact Us
Target Market(s)
IT companies looking for top engineering talent.

```html
<!DOCTYPE html>
<html lang="en">
<head>
<meta charset="utf-8">
<title>Vantrel Capability Summary</title>
<link href="https://fonts.googleapis.com/css2?family=Montserrat:wght@400;600;700;800&family=Open+Sans:wght@400;600&display=swap" rel="stylesheet">
<style>
:root{
  --navy:#1d3d6b;
  --blue:#2f67a8;
  --sky:#dfe8f3;
  --red:#c94a3c;
  --grey:#9b9b9b;
  --text:#6b6b6b;
  --white:#ffffff;
}
*{box-sizing:border-box;margin:0;padding:0}
html,body{width:716px;height:1200px;overflow:hidden}
body{position:relative;background:var(--white);font-family:"Open Sans",Arial,sans-serif}
.showcase{position:absolute;left:0;top:490px;width:716px;height:710px;background:var(--grey)}
.slide{position:absolute;width:258px;height:145px;background:var(--white);overflow:hidden;box-shadow:0 1px 3px rgba(0,0,0,.25)}
.slide--hero{left:138px;top:110px;transform:scale(1.705);transform-origin:0 0;box-shadow:0 2px 6px rgba(0,0,0,.15)}
.slide-header{position:absolute;left:0;top:8px;height:10px;width:110px;background:var(--navy);clip-path:polygon(0 0,100% 0,94% 100%,0 100%);color:var(--white);font:700 4.5px/10px Montserrat,sans-serif;padding-left:8px;letter-spacing:.3px;white-space:nowrap}
.slide-brand{position:absolute;right:10px;top:8px;font:800 7px/10px Montserrat,sans-serif;color:var(--navy);letter-spacing:.3px}
.slide-rule{position:absolute;left:110px;right:60px;top:17px;height:1px;background:var(--sky)}
.slide-footer{position:absolute;left:0;bottom:0;width:100%;height:6px;background:var(--navy)}
.page-num{position:absolute;right:8px;bottom:8px;width:6px;height:6px;background:var(--navy)}
.cover-art{position:absolute;left:0;top:0;width:150px;height:95px;background:radial-gradient(ellipse at 35% 40%,#c9d8ea 0%,#e6edf6 55%,rgba(255,255,255,0) 80%)}
.cover-accent{position:absolute;right:0;top:0;width:70px;height:145px;background:linear-gradient(120deg,rgba(201,74,60,0) 40%,rgba(201,74,60,.12) 60%,rgba(47,103,168,.12) 80%)}
.cover-name{position:absolute;left:0;width:100%;top:42px;text-align:center;font:800 38px/1 Montserrat,sans-serif;color:var(--navy);letter-spacing:1px}
.cover-title{position:absolute;left:0;width:100%;top:84px;text-align:center;font:600 7px/1 Montserrat,sans-serif;color:var(--blue)}
.cover-sub{position:absolute;left:0;width:100%;top:93px;text-align:center;font:400 4.5px/1 "Open Sans",sans-serif;color:var(--text)}
.photo{position:absolute;background:linear-gradient(135deg,#8fa3b8,#d5dde6)}
.copy{position:absolute;font-size:3.3px;line-height:4.6px;color:var(--text)}
.copy h3{font:700 4.2px/6px Montserrat,sans-serif;color:var(--navy);margin-bottom:1px}
.copy p{margin-bottom:2.5px}
.benefit{display:flex;gap:4px;margin-bottom:3px}
.benefit-icon{flex:none;width:7px;height:7px;border-radius:50%;background:var(--blue)}
.benefit h3{line-height:5px;margin:0}
.talent-intro{position:absolute;left:10px;right:10px;top:23px;font-size:3.3px;line-height:4.6px;color:var(--text)}
.talent-photo{position:absolute;left:0;top:32px;width:100%;height:107px;background:linear-gradient(180deg,#5a86b8,#a9c2dc 55%,#dde7f2)}
.talent-list{position:absolute;left:40px;right:40px;top:70px;display:flex;justify-content:space-between}
.talent{width:52px;text-align:center;font:700 3.4px/4.5px Montserrat,sans-serif;color:var(--navy)}
.talent svg{display:block;margin:0 auto 3px}
</style>
</head>
<body>

<section class="slide slide--hero" aria-label="Cover slide">
  <div class="cover-art" role="img" aria-label="Faint blue business photo backdrop"></div>
  <div class="cover-accent"></div>
  <div class="cover-name">VANTREL</div>
  <div class="cover-title">YOUR TITLE GOES HERE</div>
  <div class="cover-sub">Subtitle goes here</div>
</section>

<main class="showcase">

  <section class="slide" style="left:88px;top:25px" aria-label="Cover slide">
    <div class="cover-art" role="img" aria-label="Faint blue business photo backdrop"></div>
    <div class="cover-accent"></div>
    <div class="cover-name">VANTREL</div>
    <div class="cover-title">YOUR TITLE GOES HERE</div>
    <div class="cover-sub">Subtitle goes here</div>
  </section>

  <section class="slide" style="left:370px;top:25px" aria-label="About us">
    <div class="slide-header">ABOUT US</div>
    <div class="slide-rule"></div>
    <div class="slide-brand">VANTREL</div>
    <div class="photo" style="left:10px;top:26px;width:118px;height:92px" role="img" aria-label="Team working at computer monitors in an office"></div>
    <div class="copy" style="left:138px;top:28px;width:110px">
      <h3>WHO WE ARE</h3>
      <p>Vantrel places cleared technical talent with innovative government contracting firms nationwide, serving small and large teams across the Federal IT market.</p>
      <p>We pair deep security-cleared networks with a data-driven recruiting process, so every search moves quickly from sourcing to a signed offer.</p>
      <p>Our recruiters understand engineering work and speak the language of the people we place.</p>
      <p>Clients rely on us as the go-to talent partner for mission-critical roles.</p>
    </div>
    <div class="page-num"></div>
    <div class="slide-footer"></div>
  </section>

  <section class="slide" style="left:88px;top:247px" aria-label="The Vantrel difference">
    <div class="slide-header">THE VANTREL DIFFERENCE</div>
    <div class="slide-rule"></div>
    <div class="slide-brand">VANTREL</div>
    <div class="copy" style="left:12px;top:28px;width:110px">
      <h3>CLEARED TALENT FIRST</h3>
      <p>We focus only on cleared technical professionals, building long relationships with engineers who already hold the access your programs need.</p>
      <p>Our bench covers network, software, data and security roles across the country.</p>
      <h3>DATA-DRIVEN SEARCH</h3>
      <p>Sourcing, data discovery and automated outreach narrow the field before any interview begins.</p>
    </div>
    <div class="copy" style="left:136px;top:28px;width:110px">
      <h3>EMPLOYEES, NOT CONTRACTORS</h3>
      <p>Unlike many recruiting firms, we give every placed employee real benefits, which keeps retention high and projects steady.</p>
      <p>Candidates join us knowing they are valued for the long term.</p>
      <h3>PROVEN PROCESS</h3>
      <p>Qualification and technical interviews confirm fit, then offer and on-boarding follow without delay.</p>
    </div>
    <div class="page-num"></div>
    <div class="slide-footer"></div>
  </section>

  <section class="slide" style="left:370px;top:247px" aria-label="Benefits we offer">
    <div class="slide-header">BENEFITS WE OFFER</div>
    <div class="slide-rule"></div>
    <div class="slide-brand">VANTREL</div>
    <div class="photo" style="left:0;top:24px;width:120px;height:115px;clip-path:polygon(0 0,100% 0,70% 100%,0 100%);background:linear-gradient(135deg,#1d3d6b,#4f7fb6)" role="img" aria-label="Blue technology photo"></div>
    <div class="copy" style="left:130px;top:25px;width:118px">
      <div class="benefit"><span class="benefit-icon"></span><div><h3>GENEROUS PTO</h3>Paid time off for every employee, from their first day on the job.</div></div>
      <div class="benefit"><span class="benefit-icon"></span><div><h3>100% VESTING 401K</h3>Retirement savings that are fully vested from day one.</div></div>
      <div class="benefit"><span class="benefit-icon"></span><div><h3>HEALTHCARE BENEFITS</h3>Medical coverage for all employees, not just a few.</div></div>
      <div class="benefit"><span class="benefit-icon"></span><div><h3>CAREER GROWTH</h3>Support for training, certifications and clearances.</div></div>
      <div class="benefit"><span class="benefit-icon"></span><div><h3>DEDICATED SUPPORT</h3>A recruiter who stays in touch after placement.</div></div>
    </div>
    <div class="page-num"></div>
    <div class="slide-footer"></div>
  </section>

  <section class="slide" style="left:229px;top:470px" aria-label="The talent we work with">
    <div class="slide-header">THE TALENT WE WORK WITH</div>
    <div class="slide-rule"></div>
    <div class="slide-brand">VANTREL</div>
    <div class="talent-intro">We place cleared engineers in network and systems, software development, data science and information assurance roles.</div>
    <div class="talent-photo" role="img" aria-label="Silhouetted team in a bright office"></div>
    <div class="talent-list">
      <div class="talent"><svg width="16" height="16" viewBox="0 0 16 16"><circle cx="8" cy="8" r="7.5" fill="#fff"/><rect x="4" y="5" width="8" height="5" fill="none" stroke="#1d3d6b"/><line x1="6" y1="12" x2="10" y2="12" stroke="#1d3d6b"/></svg>NETWORK &amp; SYSTEMS ENGINEERING</div>
      <div class="talent"><svg width="16" height="16" viewBox="0 0 16 16"><circle cx="8" cy="8" r="7.5" fill="#fff"/><path d="M6 5 3.5 8 6 11M10 5l2.5 3L10 11" fill="none" stroke="#1d3d6b"/></svg>SOFTWARE DEVELOPMENT</div>
      <div class="talent"><svg width="16" height="16" viewBox="0 0 16 16"><circle cx="8" cy="8" r="7.5" fill="#fff"/><path d="M4 11h8M5 11V8M8 11V5M11 11V7" stroke="#1d3d6b" fill="none"/></svg>DATA SCIENCE</div>
    </div>
    <div class="page-num"></div>
    <div class="slide-footer"></div>
  </section>

</main>
</body>
</html>
```